Bright Arrow Delivery Service Wordpress design

My client is a delivery service whose motto is "We go where the freight leads us." Their colors are red, white and blue. They use Voyalo vans and box vans - NO semi tractors. They like this Website design www.tovamu-sample.com, but I would like to see some designs that make them stand out. Attached is their new logo.

Target Market(s)

Businesses who use delivery services in town and anyone needing freight picked up or transported in the United States.

Industry/Entity Type

Delivery Service

Number of Pages Required

1 page

Font styles to use
Sans Serif

Colors
ec1f27
0455a3
ffffff

Requirements
Must have
• We need a Wordpress design with sliders that incorporates their new logo and the motto "WE GO WHERE THE FREIGHT LEADS US" Their corporate colors are red, white and blue. They only use voyalo vans and box vans.
Nice to have
• Please use your creativity to come up with a unique design for this delivery service.
Should not have
• NO SEMI TRACTOR TRAILERS

```html
<!DOCTYPE html>
<html lang="en">
<head>
<meta charset="utf-8">
<title>Bright Arrow Express Delivery</title>
<link href="https://fonts.googleapis.com/css2?family=Raleway:wght@600;700;800&family=Lato:wght@400;700;900&display=swap" rel="stylesheet">
<style>
:root{
  --navy:#1c1766;
  --navy-dark:#2a2752;
  --red:#e51f26;
  --white:#ffffff;
  --ink:#222222;
  --grey:#5a5a5a;
  --pale:#eef0f4;
  --dark:#2b2b2b;
  --footer:#1e1e1e;
}
*{box-sizing:border-box;margin:0;padding:0}
html,body{width:1200px;height:2804px;overflow:hidden}
body{font-family:"Lato",sans-serif;color:var(--ink);background:var(--white)}
.page{position:relative;width:1200px;height:2804px;overflow:hidden}
.abs{position:absolute}
h2,h3,.display{font-family:"Raleway",sans-serif}

/* top bar */
.topbar{left:0;top:0;width:1200px;height:46px;background:var(--navy-dark)}
.topbar .social{left:106px;top:14px;display:flex;gap:12px}
.topbar .social span{width:16px;height:16px;border-radius:50%;background:var(--white);display:block}
.topbar .phone{left:652px;top:12px;color:var(--white);font-weight:700;font-size:20px;display:flex;align-items:center;gap:10px;white-space:nowrap}
.topbar .quote-btn{left:876px;top:0;width:216px;height:40px;background:var(--red);color:var(--white);font-family:"Raleway",sans-serif;font-weight:700;font-size:22px;display:flex;align-items:center;justify-content:center;white-space:nowrap}

/* header */
.header{left:0;top:46px;width:1200px;height:84px;background:var(--white);box-shadow:0 2px 6px rgba(0,0,0,.15)}
.brand{left:92px;top:14px;display:flex;align-items:center;gap:14px}
.brand .mark{width:52px;height:52px;background:var(--navy);border-radius:50%}
.brand .name{font-family:"Lato",sans-serif;font-weight:900;font-size:24px;color:var(--navy);line-height:1.05}
.brand .name small{display:block;font-size:10px;letter-spacing:1px}
.nav{right:106px;top:22px;display:flex;gap:40px;font-family:"Lato",sans-serif;font-weight:700;font-size:20px}
.nav a{color:var(--ink);text-decoration:none;padding-bottom:6px}
.nav a.active{color:var(--red);border-bottom:2px solid var(--red)}

/* hero */
.hero{left:0;top:130px;width:1200px;height:592px;background:linear-gradient(90deg,#3b3d44 0%,#6b6258 45%,#a88f55 75%,#5e5a4e 100%)}
.hero-title{left:102px;top:352px;color:var(--white);font-weight:700;font-size:42px;line-height:56px;letter-spacing:.5px;white-space:nowrap}
.hero-btn{left:108px;top:472px;width:222px;height:44px;border-radius:22px;background:var(--red);color:var(--white);font-family:"Raleway",sans-serif;font-weight:800;font-size:21px;display:flex;align-items:center;justify-content:space-between;padding:0 4px 0 14px;border:2px solid var(--white);white-space:nowrap}
.hero-btn i{width:34px;height:34px;border-radius:50%;border:2px solid var(--white);display:flex;align-items:center;justify-content:center;flex:none}
.arrow-l,.arrow-r{top:400px}
.arrow-l{left:24px}.arrow-r{right:24px}

/* section titles */
.sec-title{left:0;width:1200px;text-align:center;font-weight:800;font-size:36px;color:var(--navy);letter-spacing:.5px}
.sec-title span{color:var(--red)}
.divider{left:320px;width:560px;height:26px}

/* services */
.services{left:0;top:722px;width:1200px;height:508px;background:linear-gradient(135deg,#eef0f4,#ffffff 40%,#e8eaef 70%,#f6f7f9)}
.card{top:883px;width:244px}
.card .photo{width:244px;height:152px;border-radius:4px}
.card .tag{margin-top:14px;font-style:italic;font-size:13px;color:var(--grey)}
.card h3{font-family:"Lato",sans-serif;font-weight:900;font-size:21px;color:var(--navy);margin-top:4px}
.card p{font-size:13px;line-height:19px;color:#333;margin-top:8px}

/* about */
.about{left:0;top:1230px;width:1200px;height:490px;background:linear-gradient(135deg,#f3f4f7,#ffffff 50%,#eceef2)}
.about-photo{left:80px;top:1258px;width:318px;height:390px;background:linear-gradient(160deg,#c9ccd2,#8b93a3 55%,#b08a5a)}
.about-frame{left:90px;top:1266px;width:298px;height:374px;border:3px solid var(--white)}
.about-body{left:435px;top:1256px;width:350px}
.about-body h2{font-weight:800;font-size:32px;color:var(--navy)}
.about-body h2 span{color:var(--red)}
.about-body .lead{font-size:14px;line-height:22px;margin-top:10px;color:#333}
.feature{display:flex;gap:16px;padding:14px 0 12px;border-bottom:1px solid #d4d6da}
.feature:last-child{border-bottom:none}
.feature .ico{width:40px;flex:none}
.feature h4{font-family:"Lato",sans-serif;font-weight:900;font-size:17px}
.feature p{font-size:12.5px;line-height:17px;color:#333;margin-top:4px}

.quote-form{left:828px;top:1258px;width:292px;height:400px}
.quote-form .label{display:inline-block;background:var(--red);color:var(--white);font-weight:700;font-size:17px;padding:6px 10px}
.quote-form .box{background:var(--navy);padding:10px 12px 12px;height:326px;color:var(--white)}
.quote-form label{display:block;font-weight:700;font-size:14px;margin:6px 0 5px}
.quote-form .field{background:var(--white);height:32px;font-size:11px;font-style:italic;color:#888;padding:9px 8px}
.quote-form .row{display:flex;gap:14px}
.quote-form .row>div{flex:1}
.quote-form .msg{height:78px}
.quote-form .submit{background:var(--red);color:var(--white);font-weight:900;font-size:17px;height:38px;display:flex;align-items:center;justify-content:center}

/* testimonials */
.testimonials{left:0;top:1720px;width:1200px;height:430px;background:linear-gradient(180deg,#2e2e2e,#3a3a3a 60%,#2a2a2a)}
.quote-card{top:1895px;width:328px;height:180px;background:rgba(20,20,20,.75);padding:22px 22px 0 60px;color:#cfcfcf}
.quote-card .qm{position:absolute;left:14px;top:10px;font-family:"Raleway",sans-serif;font-size:64px;color:#555;line-height:1}
.quote-card p{font-size:13.5px;line-height:20px}
.quote-card .who{text-align:right;margin-top:26px;color:var(--red);font-weight:900;font-size:15px}
.quote-card .role{text-align:right;font-size:12px;color:#555}

/* newsletter */
.newsletter{left:0;top:2150px;width:1200px;height:330px;background:linear-gradient(135deg,#eef0f4,#ffffff 45%,#e9ebf0)}
.news-text{left:120px;top:2280px;width:960px;text-align:center;font-size:16px;line-height:26px;color:#222}
.news-form{left:345px;top:2368px;width:595px;height:42px;display:flex;border:1px solid #999}
.news-form .input{flex:1;background:var(--white);font-size:13px;padding:13px 14px;color:#333}
.news-form .btn{width:165px;background:var(--navy);color:var(--white);font-weight:900;font-size:17px;display:flex;align-items:center;justify-content:center;gap:10px}
.news-form .btn i{width:26px;height:26px;border-radius:50%;background:var(--red);display:flex;align-items:center;justify-content:center}

/* footer */
.footer{left:0;top:2480px;width:1200px;height:276px;background:var(--footer);border-top:4px solid var(--red)}
.foot-col{color:var(--white)}
.foot-h{font-family:"Lato",sans-serif;font-size:22px;font-weight:400;color:var(--white)}
.foot-h span{color:var(--red)}
.foot-line{height:1px;background:#444;margin-top:10px}
.links{left:100px;top:2510px;width:140px}
.links ul{list-style:none;margin-top:14px}
.links li{font-size:14px;line-height:31px;color:var(--white)}
.links li::before{content:"• "}
.contact{left:295px;top:2510px;width:600px}
.contact .addr{font-size:14.5px;line-height:20px;margin-top:16px;width:240px;color:var(--white)}
.contact .line{display:flex;align-items:center;gap:10px;font-size:14px;margin-top:15px;color:var(--white)}
.map{left:556px;top:2566px;width:346px;height:160px;background:linear-gradient(135deg,#d8d4c4,#bcd0e0 50%,#e3dfcf)}
.follow{left:967px;top:2510px;width:140px}
.follow .item{display:flex;align-items:center;gap:10px;font-size:12px;font-weight:700;margin-top:12px;color:var(--white)}
.follow .item:first-of-type{margin-top:18px}
.follow .dot{width:32px;height:32px;border-radius:50%;background:var(--navy);flex:none}
.follow .dot.red{background:#c7352a}
.copyright{left:0;top:2756px;width:1200px;height:48px;background:var(--red);color:var(--white);font-size:13px;font-weight:700;display:flex;align-items:center;justify-content:center}
</style>
</head>
<body>
<div class="page">

  <div class="abs topbar">
    <div class="abs social"><span></span><span></span><span></span><span></span></div>
    <div class="abs phone">
      <svg width="20" height="20" viewBox="0 0 20 20"><circle cx="10" cy="10" r="9" fill="none" stroke="#fff" stroke-width="1.5"/><path d="M7 5l2 2-1 1.5c.6 1.4 1.6 2.4 3 3L12.5 10l2 2-1.5 2C9.5 13.5 6.5 10.5 6 7z" fill="#fff"/></svg>
      123 - 456 - 7890
    </div>
    <div class="abs quote-btn">REQUEST A QUOTE</div>
  </div>

  <header class="abs header">
    <div class="abs brand">
      <div class="name">BRIGHT ARROW<small>EXPRESS DELIVERY · WE GO WHERE THE FREIGHT LEADS US</small></div>
      <div class="mark"></div>
    </div>
    <nav class="abs nav">
      <a class="active" href="#">Home</a><a href="#">About Us</a><a href="#">Services</a><a href="#">Resources</a><a href="#">Contact Us</a>
    </nav>
  </header>

  <section class="abs hero" role="img" aria-label="Smiling courier leaning on stacked parcels on a hand truck in front of a row of yellow delivery vans"></section>
  <svg class="abs arrow-l" width="22" height="60" viewBox="0 0 22 60"><path d="M20 2L2 30l18 28" fill="none" stroke="rgba(255,255,255,.5)" stroke-width="2"/></svg>
  <svg class="abs arrow-r" width="22" height="60" viewBox="0 0 22 60"><path d="M2 2l18 28L2 58" fill="none" stroke="rgba(255,255,255,.5)" stroke-width="2"/></svg>
  <h1 class="abs hero-title display">WE GO WHERE<br>THE FREIGHT LEADS US</h1>
  <div class="abs hero-btn">GET A QUOTE <i><svg width="14" height="14" viewBox="0 0 14 14"><path d="M2 2l5 5-5 5M7 2l5 5-5 5" fill="none" stroke="#fff" stroke-width="2"/></svg></i></div>

  <section class="abs services"></section>
  <h2 class="abs sec-title" style="top:758px">OUR <span>SERVICES</span></h2>
  <svg class="abs divider" style="top:822px" viewBox="0 0 560 26"><line x1="0" y1="13" x2="560" y2="13" stroke="#999"/><circle cx="280" cy="13" r="12" fill="#fff" stroke="#999"/></svg>

  <article class="abs card" style="left:80px">
    <div class="photo" role="img" aria-label="Courier handing a parcel to a customer at her door" style="background:linear-gradient(135deg,#d9c8b0,#b9a48a 60%,#8fa0b5)"></div>
    <div class="tag">24h a day</div><h3>Courier Delivery</h3>
    <p>Duis hendrerit est nec eleifend euismod. Nulla tristique suscipit lacinia. Fusce vel vestibulum nulla.</p>
  </article>
  <article class="abs card" style="left:345px">
    <div class="photo" role="img" aria-label="Delivery worker passing a box to an office client" style="background:linear-gradient(135deg,#cfd3da,#a08a70 55%,#d33a36)"></div>
    <div class="tag">New service</div><h3>B2B Services</h3>
    <p>Duis hendrerit est nec eleifend euismod. Nulla tristique suscipit lacinia. Fusce vel vestibulum nulla.</p>
  </article>
  <article class="abs card" style="left:610px">
    <div class="photo" role="img" aria-label="Cargo plane, cargo ship and delivery vans showing logistics" style="background:linear-gradient(180deg,#e6eef6,#bcd0e4 55%,#6f9bc7)"></div>
    <div class="tag">7 days a week</div><h3>Logistics</h3>
    <p>Duis hendrerit est nec eleifend euismod. Nulla tristique suscipit lacinia. Fusce vel vestibulum nulla.</p>
  </article>
  <article class="abs card" style="left:875px">
    <div class="photo" role="img" aria-label="Courier carrying a parcel in front of an office building" style="background:linear-gradient(135deg,#9fb3c8,#c8b08c 55%,#6f84a0)"></div>
    <div class="tag">24h a day</div><h3>Same Day Services</h3>
    <p>Duis hendrerit est nec eleifend euismod. Nulla tristique suscipit lacinia. Fusce vel vestibulum nulla.</p>
  </article>

  <section class="abs about"></section>
  <div class="abs about-photo" role="img" aria-label="Delivery man in uniform carrying parcels and a clipboard"></div>
  <div class="abs about-frame"></div>
  <div class="abs about-body">
    <h2>ABOUT <span>US</span></h2>
    <p class="lead">Lorem ipsum dolor sit amet, consectetuer adipiscing elit, sed diam nonummy nibh euismod tincidunt ut laoreet dolore magna aliquam erat volutpat. Ut wisi enim ad minim veniam, quis nostrud exerci.</p>
    <div class="feature">
      <svg class="ico" viewBox="0 0 40 26" height="26"><rect x="8" y="3" width="18" height="14" fill="#e51f26"/><path d="M26 7h7l5 5v5H26z" fill="#e51f26"/><circle cx="14" cy="20" r="3.5" fill="#e51f26"/><circle cx="32" cy="20" r="3.5" fill="#e51f26"/><path d="M0 6h6M2 10h5M0 14h6" stroke="#e51f26" stroke-width="2"/></svg>
      <div><h4>Fast Delivery</h4><p>Lorem ipsum dolor sit amet, consectetuer adipiscing dolore magna volutpat.</p></div>
    </div>
    <div class="feature">
      <svg class="ico" viewBox="0 0 40 40" height="40"><circle cx="20" cy="20" r="17" fill="none" stroke="#e51f26" stroke-width="3"/><text x="20" y="25" text-anchor="middle" font-family="Lato,sans-serif" font-weight="900" font-size="13" fill="#e51f26">24h</text></svg>
      <div><h4>24 Hours Support</h4><p>Lorem ipsum dolor sit amet, consectetuer adipiscing dolore magna volutpat.</p></div>
    </div>
    <div class="feature">
      <svg class="ico" viewBox="0 0 40 40" height="36"><circle cx="20" cy="13" r="8" fill="#e51f26"/><path d="M6 38c0-9 6-14 14-14s14 5 14 14z" fill="#e51f26"/><path d="M10 13a10 10 0 0 1 20 0" fill="none" stroke="#e51f26" stroke-width="2"/></svg>
      <div><h4>Direct Client Contact</h4><p>Lorem ipsum dolor sit amet, consectetuer adipiscing dolore magna volutpat.</p></div>
    </div>
  </div>

  <form class="abs quote-form">
    <div class="label">GET A Quick Quote</div>
    <div class="box">
      <label>Name</label><div class="field">Name</div>
      <label>Email Address</label><div class="field">Email</div>
      <div class="row">
        <div><label>Select Service</label><div class="field">Select ▾</div></div>
        <div><label>Select Date</label><div class="field">dd/mm/yy</div></div>
      </div>
      <label>Message</label><div class="field msg"></div>
    </div>
    <div class="submit">SUBMIT</div>
  </form>

  <section class="abs testimonials" aria-label="Client testimonials"></section>
  <h2 class="abs sec-title" style="top:1758px;color:#fff">CLIENT TESTIMONIALS</h2>
  <svg class="abs divider" style="top:1822px" viewBox="0 0 560 26"><line x1="0" y1="13" x2="560" y2="13" stroke="#666"/><circle cx="280" cy="13" r="12" fill="#333" stroke="#777"/></svg>

  <div class="abs quote-card" style="left:80px"><span class="qm">“</span>
    <p>Lorem ipsum dolor sit amet, consectet uer adipiscing elit, sed diam nonummy nibh euis mod tincidun nt ut laoreetml dolore magna aliquam erat volutpat.</p>
    <div class="who">Mara Lindqvist</div><div class="role">CTO of Norvane Air</div></div>
  <div class="abs quote-card" style="left:436px"><span class="qm">“</span>
    <p>Lorem ipsum dolor sit amet, consectet uer adipiscing elit, sed diam nonummy nibh euis mod tincidun nt ut laoreetml dolore magna aliquam erat volutpat.</p>
    <div class="who">Owen Tate</div><div class="role">Halden Build LLC</div></div>
  <div class="abs quote-card" style="left:792px"><span class="qm">“</span>
    <p>Lorem ipsum dolor sit amet, consectet uer adipiscing elit, sed diam nonummy nibh euis mod tincidun nt ut laoreetml dolore magna aliquam erat volutpat.</p>
    <div class="who">Iris Calloway</div><div class="role">Quillo General Manager</div></div>

  <section class="abs newsletter"></section>
  <h2 class="abs sec-title" style="top:2180px">NEWSLETTER <span>SIGN UP</span></h2>
  <svg class="abs divider" style="top:2240px" viewBox="0 0 560 26"><line x1="0" y1="13" x2="560" y2="13" stroke="#999"/><circle cx="280" cy="13" r="12" fill="#fff" stroke="#999"/></svg>
  <p class="abs news-text">Lorem ipsum dolor sit amet, consectetuer adipiscing elit, sed diam nonummy nibh euismod tincidunt ut laoreet dolore magna aliquam erat volutpat. Ut wisi enim ad minim veniam.</p>
  <svg class="abs" style="left:250px;top:2308px" width="100" height="80" viewBox="0 0 100 80"><path d="M4 4l62 6-36 22z" fill="#e51f26"/><path d="M30 32c-20 10-10 30 10 34s40 6 60 8" fill="none" stroke="#777" stroke-dasharray="3 4"/></svg>
  <div class="abs news-form">
    <div class="input">Enter your email address</div>
    <div class="btn">SUBSCRIBE <i><svg width="12" height="12" viewBox="0 0 14 14"><path d="M2 2l5 5-5 5M7 2l5 5-5 5" fill="none" stroke="#fff" stroke-width="2"/></svg></i></div>
  </div>

  <footer class="abs footer"></footer>
  <div class="abs links foot-col">
    <div class="foot-h">Quick <span>Links</span></div><div class="foot-line"></div>
    <ul><li>Home</li><li>About Us</li><li>Services</li><li>Resources</li><li>Contact Us</li></ul>
  </div>
  <div class="abs contact foot-col">
    <div class="foot-h">Contact <span>Detail</span></div><div class="foot-line" style="width:230px"></div>
    <div class="addr">Bright Arrow Express Delivery<br>123, Ut wisi enim ad minim veniam, Mor nostmi tation -123 456</div>
    <div class="line"><svg width="14" height="14" viewBox="0 0 14 14"><path d="M3 1l3 3-1.5 2c.8 1.5 2 2.7 3.5 3.5L10 8l3 3-2 2C6 12 2 8 1 3z" fill="#e51f26"/></svg>(123) 456 7890</div>
    <div class="line"><svg width="14" height="14" viewBox="0 0 14 14"><rect x="3" y="1" width="8" height="4" fill="#e51f26"/><rect x="1" y="5" width="12" height="6" fill="#e51f26"/><rect x="3" y="9" width="8" height="4" fill="#e51f26"/></svg>(123) 456 7890</div>
    <div class="line"><svg width="14" height="12" viewBox="0 0 14 12"><rect x="1" y="1" width="12" height="10" fill="#e51f26"/><path d="M1 1l6 5 6-5" fill="none" stroke="#1e1e1e"/></svg>info@brightarrowdelivery-sample.com</div>
  </div>
  <div class="abs map" role="img" aria-label="Street map of the office location with a red pin"></div>
  <div class="abs follow foot-col">
    <div class="foot-h">Follow <span>Us</span></div><div class="foot-line"></div>
    <div class="item"><span class="dot"></span>FRIENDWALL</div>
    <div class="item"><span class="dot"></span>CHIRPLY</div>
    <div class="item"><span class="dot"></span>WORKLINE</div>
    <div class="item"><span class="dot red"></span>Circlespace</div>
  </div>
  <div class="abs copyright">Copyright © 2016 Bright Arrow Express Delivery . All Rights Reserved.</div>

</div>
</body>
</html>
```